Redesign of an insurance website

Attached is an insurance website that I need to redesign. Currently the website is too dark. I like for example www.brenvalo.com . Could you make the website lighter and change the structure a little so that it is more user friendly?

Industry/Entity Type

Insurance

Number of Pages Required

4 page

```html
<!DOCTYPE html>
<html lang="en">
<head>
<meta charset="utf-8">
<title>Krytovka.cz – Insurance</title>
<link rel="stylesheet" href="https://fonts.googleapis.com/css2?family=Poppins:wght@300;400;500;600&display=swap">
<style>
:root{
  --blue:#29b6e8;
  --blue-dark:#1ea8da;
  --ink:#1a1a1a;
  --text:#333;
  --hero-bg:#f3f3f4;
  --row-bg:#f6f6f6;
  --line:#d9d9d9;
  --white:#fff;
}
*{box-sizing:border-box;margin:0;padding:0}
html,body{width:1083px;height:1200px;overflow:hidden}
body{font-family:'Poppins',sans-serif;color:var(--text);background:var(--white);position:relative}
.abs{position:absolute}

.topbar{left:0;top:0;width:1083px;height:27px;background:var(--blue)}
.social{left:106px;top:8px;display:flex;gap:9px}
.social span{width:10px;height:10px;border-radius:50%;background:var(--white);display:block}
.account{right:108px;top:6px;display:flex;gap:12px;font-size:10.5px;color:var(--white)}
.account span{display:flex;align-items:center;gap:4px}
.account .sep{width:1px;height:14px;background:rgba(255,255,255,.5)}

.header{left:0;top:27px;width:1083px;height:51px;background:#f7fbfd;border-bottom:1px solid #eee}
.search{left:109px;top:21px;width:118px;height:23px;border:1.5px solid #e3e3e3;border-radius:12px;background:var(--white);font-size:9.5px;color:#777;padding:4px 0 0 13px}
.search svg{position:absolute;right:12px;top:5px}
.logo{left:0;width:1083px;top:22px;text-align:center;font-weight:600;font-size:21px;color:var(--ink);letter-spacing:.5px}
.logo i{display:inline-block;width:9px;height:9px;border-radius:50%;background:var(--blue);margin-right:6px;vertical-align:3px}
.nav{right:108px;top:31px;display:flex;gap:15px;font-size:12.5px;color:var(--ink)}

.hero{left:0;top:78px;width:1083px;height:462px;background:var(--hero-bg)}
.hero-photo{left:145px;top:78px;width:295px;height:462px;background:linear-gradient(180deg,#e9eef3 0%,#c9dcee 55%,#a9c6e2 100%)}
.hero-h1{left:500px;width:424px;top:148px;text-align:center;font-size:24px;font-weight:400;color:var(--ink);letter-spacing:.5px}
.hero-h2{left:480px;width:464px;top:178px;text-align:center;font-size:34px;font-weight:600;color:var(--blue);letter-spacing:1px}
.type{text-align:center;font-size:12.5px;color:var(--ink)}
.type .ring{border:3px solid var(--ink);border-radius:50%;display:flex;align-items:center;justify-content:center;background:var(--white)}
.type.active{color:var(--blue)}
.type.active .ring{border:none;background:var(--blue)}
.arrow{font-size:20px;color:#aaa;top:284px}
.form-title{left:500px;width:424px;top:392px;text-align:center;font-size:18px;font-weight:500;color:var(--ink)}
.zip{left:551px;top:431px;width:323px;height:35px;border:1px solid #cfcfcf;border-radius:18px;background:var(--white);font-size:12.5px;color:var(--ink);padding:8px 0 0 42px}
.zip svg{position:absolute;left:22px;top:10px}
.btn{border-radius:18px;color:var(--white);font-size:13px;font-weight:500;display:flex;align-items:center;justify-content:center;letter-spacing:.3px}
.btn-quote{left:726px;top:431px;width:148px;height:35px;background:var(--blue)}

.reasons-title{left:0;width:1083px;top:562px;text-align:center;font-size:27px;font-weight:500;color:var(--ink);letter-spacing:.5px;z-index:2}
.reasons-title b{color:var(--blue);font-weight:600}
.accordion{left:110px;top:633px;width:429px}
.acc-head{height:33px;background:var(--blue);color:var(--white);font-size:12.5px;display:flex;align-items:center;justify-content:space-between;padding:0 14px}
.acc-body{font-size:11px;line-height:18.5px;color:var(--ink);padding:8px 14px 9px 13px}
.acc-row{height:33px;background:var(--row-bg);margin-bottom:2px;font-size:12.5px;color:var(--ink);display:flex;align-items:center;justify-content:space-between;padding:0 14px}
.reasons-photo{left:552px;top:606px;width:424px;height:378px;background:linear-gradient(180deg,#ffffff 0%,#dde9f5 45%,#a8c7e6 100%);z-index:1}

.news-band{left:0;top:984px;width:1083px;height:216px;background:linear-gradient(135deg,#58c4ec 0%,#3eb6e6 50%,#5fc6ee 100%)}
.news-card{left:150px;top:1010px;width:776px;height:128px;background:var(--white);border-radius:10px}
.news-title{left:194px;top:1046px;font-size:22px;font-weight:600;color:var(--blue);letter-spacing:.5px}
.news-sub{left:194px;top:1075px;font-size:15px;color:var(--ink)}
.email{left:458px;top:1058px;width:270px;height:35px;border:1px solid #cfcfcf;border-radius:18px 0 0 18px;border-right:none;font-size:11.5px;color:var(--ink);padding:9px 0 0 25px}
.btn-sub{left:710px;top:1058px;width:172px;height:35px;background:var(--ink);font-size:13px}
.footer-line{left:0;top:1164px;width:1083px;height:1px;background:rgba(255,255,255,.35)}
.copy{left:0;width:1083px;top:1174px;text-align:center;font-size:11.5px;color:var(--white)}
</style>
</head>
<body>
<div class="abs topbar"></div>
<div class="abs social"><span></span><span></span><span></span><span></span></div>
<div class="abs account">
  <span><svg width="9" height="10" viewBox="0 0 9 10"><circle cx="4.5" cy="2.6" r="2.4" fill="#fff"/><path d="M0 10c0-3 2-4.5 4.5-4.5S9 7 9 10z" fill="#fff"/></svg>SIGN IN</span>
  <span class="sep"></span>
  <span><svg width="8" height="10" viewBox="0 0 8 10"><path d="M2 4V3a2 2 0 0 1 4 0v1" stroke="#fff" stroke-width="1.3" fill="none"/><rect x="0" y="4" width="8" height="6" rx="1" fill="#fff"/></svg>SIGN UP</span>
</div>

<header class="abs header">
  <div class="abs search">Search...
    <svg width="11" height="11" viewBox="0 0 11 11"><circle cx="4.5" cy="4.5" r="3.5" stroke="#29b6e8" stroke-width="1.8" fill="none"/><path d="M7 7l3 3" stroke="#29b6e8" stroke-width="2"/></svg>
  </div>
  <div class="abs logo"><i></i>KRYTOVKA.CZ</div>
  <nav class="abs nav"><span>ABOUT US</span><span>FAQ'S</span><span>CONTACT US</span></nav>
</header>

<section class="abs hero"></section>
<div class="abs hero-photo" role="img" aria-label="Photo of a smiling woman in a light blue shirt giving a thumbs up"></div>
<h1 class="abs hero-h1">CHOOSE ANY TYPE OF</h1>
<h2 class="abs hero-h2">INSURANCE YOU WANT</h2>

<div class="abs arrow" style="left:527px">&#8249;</div>
<div class="abs arrow" style="left:885px;color:var(--blue)">&#8250;</div>

<div class="abs type" style="left:563px;top:262px;width:72px">
  <div class="ring" style="width:72px;height:72px">
    <svg width="36" height="36" viewBox="0 0 24 24"><path d="M21 3c-1-1-2.5-.5-3.5.5L14 7 5 5 3.5 6.5 11 10l-3.5 3.5L5 13l-1 1 3 2 2 3 1-1-.5-2.5L13 12l3.5 7.5L18 18l-2-9 3.5-3.5c1-1 1.5-2.5.5-3.5z" fill="#1a1a1a"/></svg>
  </div>
  <div style="margin-top:1px">Travel</div>
</div>
<div class="abs type active" style="left:662px;top:248px;width:100px">
  <div class="ring" style="width:100px;height:100px">
    <svg width="60" height="40" viewBox="0 0 60 40"><path d="M10 18l5-12c1-2 3-3 5-3h20c2 0 4 1 5 3l5 12c3 1 5 3 5 6v9c0 1-1 2-2 2H7c-1 0-2-1-2-2v-9c0-3 2-5 5-6z" fill="#fff"/><path d="M16 17l3-9c.5-1 1.5-1.5 2.5-1.5h17c1 0 2 .5 2.5 1.5l3 9z" fill="#29b6e8"/><circle cx="14" cy="25" r="3.5" fill="#29b6e8"/><circle cx="46" cy="25" r="3.5" fill="#29b6e8"/><rect x="22" y="24" width="16" height="3" rx="1.5" fill="#29b6e8"/><rect x="8" y="34" width="9" height="6" rx="2" fill="#fff"/><rect x="43" y="34" width="9" height="6" rx="2" fill="#fff"/></svg>
  </div>
  <div style="margin-top:4px;font-size:13.5px">Auto</div>
</div>
<div class="abs type" style="left:790px;top:262px;width:72px">
  <div class="ring" style="width:72px;height:72px">
    <svg width="40" height="34" viewBox="0 0 40 34"><circle cx="12" cy="8" r="6" fill="#1a1a1a"/><circle cx="28" cy="8" r="6" fill="#1a1a1a"/><path d="M2 32c0-10 4-16 10-16s10 6 10 16z" fill="#1a1a1a"/><path d="M18 32c0-10 4-16 10-16s10 6 10 16z" fill="#1a1a1a"/><circle cx="20" cy="19" r="4" fill="#fff"/><path d="M13 33c0-6 3-9 7-9s7 3 7 9z" fill="#fff"/></svg>
  </div>
  <div style="margin-top:2px">Life</div>
</div>

<div class="abs form-title">AUTO INSURANCE</div>
<div class="abs zip">
  <svg width="11" height="14" viewBox="0 0 11 14"><path d="M5.5 0A5.5 5.5 0 0 0 0 5.5C0 9.5 5.5 14 5.5 14S11 9.5 11 5.5A5.5 5.5 0 0 0 5.5 0z" fill="#1a1a1a"/><circle cx="5.5" cy="5.3" r="2" fill="#fff"/></svg>
  Enter ZIP Code
</div>
<div class="abs btn btn-quote">START QUOTE</div>

<div class="abs reasons-photo" role="img" aria-label="Photo of a woman in a light blue shirt pointing to the left"></div>
<h2 class="abs reasons-title">REASONS <b>TO CHOOSE US</b></h2>
<div class="abs accordion">
  <div class="acc-head">Easy Process<svg width="11" height="7" viewBox="0 0 11 7"><path d="M1 6l4.5-4.5L10 6" stroke="#fff" stroke-width="1.6" fill="none"/></svg></div>
  <p class="acc-body">Aliquam porta ex nec arcu pharetra luctus. Integer cursus condimentum magna id finibus. Nulla mattis augue vitae bibendum scelerisque. Duis egestas egestas tempor.</p>
  <div class="acc-row">Hassle free<svg width="11" height="7" viewBox="0 0 11 7"><path d="M1 1l4.5 4.5L10 1" stroke="#333" stroke-width="1.6" fill="none"/></svg></div>
  <div class="acc-row">100% Safe and Secure<svg width="11" height="7" viewBox="0 0 11 7"><path d="M1 1l4.5 4.5L10 1" stroke="#333" stroke-width="1.6" fill="none"/></svg></div>
  <div class="acc-row">Aliquam porta ex nec arcu pharetra luctus<svg width="11" height="7" viewBox="0 0 11 7"><path d="M1 1l4.5 4.5L10 1" stroke="#333" stroke-width="1.6" fill="none"/></svg></div>
  <div class="acc-row">Integer cursus condimentum magna id<svg width="11" height="7" viewBox="0 0 11 7"><path d="M1 1l4.5 4.5L10 1" stroke="#333" stroke-width="1.6" fill="none"/></svg></div>
  <div class="acc-row">Nulla mattis augue vitae bibendum scelerisque<svg width="11" height="7" viewBox="0 0 11 7"><path d="M1 1l4.5 4.5L10 1" stroke="#333" stroke-width="1.6" fill="none"/></svg></div>
  <div class="acc-row">Pellentesque interdum venenatis bibendum<svg width="11" height="7" viewBox="0 0 11 7"><path d="M1 1l4.5 4.5L10 1" stroke="#333" stroke-width="1.6" fill="none"/></svg></div>
</div>

<section class="abs news-band" role="img" aria-label="Blue tinted background photo of people reviewing documents"></section>
<div class="abs news-card"></div>
<div class="abs news-title">SIGNUP NEWSLETTER</div>
<div class="abs news-sub">Get In Touch With Us</div>
<div class="abs email">Enter Email Address</div>
<div class="abs btn btn-sub">SUBSCRIBE NOW</div>
<div class="abs footer-line"></div>
<div class="abs copy">Copyright © 2017 Krytovka. All right reserved.</div>
</body>
</html>
```